CORTEVALDA extra virgin olive oil label

We need a label design for a new range of products dedicated to the kitchen professionals. Ideally the label will be rectangular with a H10cm L15cm
The label needs to include the following:
Cortevalda Logo
Olio Extravergine d'Oliva
1lt
Nutritional panel (see attached file)
Best before
Lot code
Product of Italy
Superior Category olive oil obtained directly from olives by mechanical processes only
Imported in Australia by
Ingredients: extra virgin olive oil
Produced and bottled by:
The final design should communicate quality, value and consistency to the kitchen professionals
The BENTU pasta sauce label can be a good example of the style we are after. see attached file

Target Market(s)

Kitchen professionals
The catch phrase is:
Bringing quality value and consistency to the kitchen professionals

This catch parse SHOULD NOT be included in the label

Industry/Entity Type

Kitchen

Font styles to use
Serif

Requirements
Must have
• Easy to read and easy to remember

```html
<!DOCTYPE html>
<html lang="en">
<head>
<meta charset="utf-8">
<title>Cortevalda Extra Virgin Olive Oil Label</title>
<link rel="stylesheet" href="https://fonts.googleapis.com/css2?family=Bodoni+Moda:wght@400;500&family=Arimo:wght@400;700&family=Roboto+Condensed:wght@400;700&display=swap">
<style>
  :root {
    --ink: #111111;
    --red: #e5202a;
    --paper: #ffffff;
    --edge: #9a9a9a;
    --shadow: rgba(0, 0, 0, 0.5);
  }
  * { margin: 0; padding: 0; box-sizing: border-box; }
  html, body { width: 1200px; height: 1000px; overflow: hidden; background: var(--paper); }
  .canvas { position: relative; width: 1200px; height: 1000px; font-family: "Arimo", Arial, sans-serif; color: var(--ink); }

  .caption { position: absolute; font-family: "Arimo", Arial, sans-serif; font-size: 14px; color: var(--ink); }
  .caption--enlarged { left: 62px; top: 353px; }
  .caption--actual { left: 1010px; top: 415px; }

  .label {
    position: absolute;
    background: var(--paper);
    border: 1px solid var(--edge);
    box-shadow: 11px 13px 10px var(--shadow);
    overflow: hidden;
  }
  .label--front { width: 482px; height: 566px; }
  .label--back { width: 368px; height: 566px; }
  .placement-front-large { left: 63px; top: 380px; }
  .placement-back-large { left: 607px; top: 380px; }
  .placement-small { transform: scale(0.5); transform-origin: 0 0; box-shadow: 16px 18px 14px var(--shadow); }
  .placement-front-small { left: 621px; top: 119px; }
  .placement-back-small { left: 893px; top: 119px; }

  /* Front */
  .brand {
    position: absolute; left: 0; right: 0; top: 82px;
    text-align: center;
    font-family: "Bodoni Moda", "Times New Roman", serif;
    font-weight: 500; font-size: 42px; letter-spacing: 1px;
    color: var(--red);
  }
  .product-name {
    position: absolute; left: 86px; top: 164px;
    font-family: "Bodoni Moda", "Times New Roman", serif;
    font-weight: 400; font-size: 45px; line-height: 50px;
    color: var(--ink);
  }
  .rule { position: absolute; left: 87px; width: 307px; height: 2px; background: var(--ink); }
  .rule--top { top: 338px; }
  .rule--bottom { top: 417px; }
  .blend {
    position: absolute; left: 87px; top: 360px;
    font-family: "Bodoni Moda", "Times New Roman", serif;
    font-size: 31px; color: var(--red); letter-spacing: 0.5px;
  }
  .process {
    position: absolute; left: 87px; top: 438px;
    font-family: "Bodoni Moda", "Times New Roman", serif;
    font-size: 29px; font-weight: 500;
  }
  .volume {
    position: absolute; left: 86px; top: 506px;
    font-family: "Bodoni Moda", "Times New Roman", serif;
    font-size: 29px; font-weight: 500;
  }
  .origin {
    position: absolute; right: 88px; top: 520px;
    font-family: "Bodoni Moda", "Times New Roman", serif;
    font-size: 17px;
  }

  /* Back */
  .ingredients {
    position: absolute; left: 0; right: 0; top: 37px;
    text-align: center; font-size: 13px; font-weight: 700; letter-spacing: -0.2px;
  }
  .nutrition {
    position: absolute; left: 88px; top: 77px; width: 193px;
    border: 1px solid var(--ink); padding: 2px 3px 3px;
    font-family: "Roboto Condensed", "Arial Narrow", sans-serif;
  }
  .nutrition__title { font-size: 19px; font-weight: 700; line-height: 19px; letter-spacing: -0.3px; }
  .nutrition__servings {
    display: flex; justify-content: space-between;
    font-size: 8.5px; font-weight: 700; line-height: 10px;
    border-bottom: 6px solid var(--ink); padding-bottom: 1px;
  }
  .nutrition__table { width: 100%; border-collapse: collapse; font-size: 7px; }
  .nutrition__table th { font-weight: 400; text-align: right; line-height: 8px; padding: 2px 0 2px; border-bottom: 3px solid var(--ink); }
  .nutrition__table td { line-height: 8px; padding: 2px 0; border-bottom: 1px solid var(--ink); text-align: right; }
  .nutrition__table td:first-child { text-align: left; font-weight: 700; }
  .nutrition__table tr.is-sub td:first-child { font-weight: 400; }
  .nutrition__table tr:last-child td { border-bottom: 6px solid var(--ink); }
  .nutrition__note { font-size: 6.5px; line-height: 7.5px; padding-top: 3px; }

  .supply {
    position: absolute; left: 0; right: 0; top: 424px;
    text-align: center; font-size: 10.5px; line-height: 13px;
  }
  .supply__head { font-weight: 400; }
  .supply__line { font-weight: 700; }
  .supply__gap { height: 5px; }
</style>
</head>
<body>
<div class="canvas">

  <p class="caption caption--enlarged">200% enlargement</p>
  <p class="caption caption--actual">Actual size</p>

  <!-- Front label, enlarged -->
  <section class="label label--front placement-front-large" aria-label="Front label">
    <p class="brand">CORTEVALDA</p>
    <h1 class="product-name">Olio<br>Extravergine<br>d'Oliva</h1>
    <div class="rule rule--top"></div>
    <p class="blend">CHEF BLEND</p>
    <div class="rule rule--bottom"></div>
    <p class="process">Cold Pressed</p>
    <p class="volume">1 litre</p>
    <p class="origin">Product of Italy</p>
  </section>

  <!-- Back label, enlarged -->
  <section class="label label--back placement-back-large" aria-label="Back label">
    <p class="ingredients">Ingredients: Extra virgin olive oil</p>
    <div class="nutrition">
      <p class="nutrition__title">Nutrition Information</p>
      <p class="nutrition__servings"><span>Servings per package: 66</span><span>Servings size: 15mL</span></p>
      <table class="nutrition__table">
        <tr><th></th><th>Quantity<br>per serving</th><th>% Daily Intake<br>per serving</th><th>Quantity<br>per 100mL</th></tr>
        <tr><td>Energy</td><td>500kJ(122Cal)</td><td>6%</td><td>3390kJ(811Cal)</td></tr>
        <tr><td>Protein</td><td>0.0g</td><td>0%</td><td>0.0g</td></tr>
        <tr><td>Fat, total</td><td>13.7g</td><td>20%</td><td>91.6g</td></tr>
        <tr class="is-sub"><td>- saturated</td><td>1.9g</td><td>8%</td><td>12.8g</td></tr>
        <tr class="is-sub"><td>- trans</td><td>LESS THAN 0.1g</td><td></td><td>LESS THAN 0.1g</td></tr>
        <tr class="is-sub"><td>- polyunsaturated</td><td>1.2g</td><td></td><td>8.2g</td></tr>
        <tr class="is-sub"><td>- omega 3</td><td>0.1g</td><td></td><td>0.7g</td></tr>
        <tr class="is-sub"><td>- monounsaturated</td><td>10.6g</td><td></td><td>70.5g</td></tr>
        <tr class="is-sub"><td>CHOLESTEROL</td><td>0mg</td><td></td><td>0mg</td></tr>
        <tr><td>Carbohydrate</td><td>0.0g</td><td>0%</td><td>0.0g</td></tr>
        <tr class="is-sub"><td>- sugars</td><td>0.0g</td><td>0%</td><td>0.0g</td></tr>
        <tr><td>Sodium</td><td>0mg</td><td>0%</td><td>0mg</td></tr>
      </table>
      <p class="nutrition__note">Note: All values are considered averages unless otherwise indicated.<br>* Percentage daily intakes are based on an average adult diet of 8700kJ. Your daily intakes may be higher or lower depending on your energy needs.</p>
    </div>
    <div class="supply">
      <p class="supply__head">Produced and bottled by</p>
      <p class="supply__line">XOXOXOXOX XOXOXOXOXOX XOXOXOXOXOOX</p>
      <p class="supply__line">OXOXOXOXOXOXO OXOXOXOXOXOX XO</p>
      <div class="supply__gap"></div>
      <p class="supply__head">Imported in Australia by</p>
      <p class="supply__line">OXOX XOXOXOXOXOX XOXOXOX</p>
      <p class="supply__line">XOXOXOXOXOXOXOXO OXOXOXOXOXOX XOXOX</p>
      <div class="supply__gap"></div>
      <p class="supply__head">Lot Code: <strong>XOXOXOXOXOXO</strong></p>
      <div class="supply__gap"></div>
      <p class="supply__head">Best before:</p>
    </div>
  </section>

  <!-- Front label, actual size -->
  <section class="label label--front placement-small placement-front-small" aria-label="Front label, actual size">
    <p class="brand">CORTEVALDA</p>
    <p class="product-name">Olio<br>Extravergine<br>d'Oliva</p>
    <div class="rule rule--top"></div>
    <p class="blend">CHEF BLEND</p>
    <div class="rule rule--bottom"></div>
    <p class="process">Cold Pressed</p>
    <p class="volume">1 litre</p>
    <p class="origin">Product of Italy</p>
  </section>

  <!-- Back label, actual size -->
  <section class="label label--back placement-small placement-back-small" aria-label="Back label, actual size">
    <p class="ingredients">Ingredients: Extra virgin olive oil</p>
    <div class="nutrition">
      <p class="nutrition__title">Nutrition Information</p>
      <p class="nutrition__servings"><span>Servings per package: 66</span><span>Servings size: 15mL</span></p>
      <table class="nutrition__table">
        <tr><th></th><th>Quantity<br>per serving</th><th>% Daily Intake<br>per serving</th><th>Quantity<br>per 100mL</th></tr>
        <tr><td>Energy</td><td>500kJ(122Cal)</td><td>6%</td><td>3390kJ(811Cal)</td></tr>
        <tr><td>Protein</td><td>0.0g</td><td>0%</td><td>0.0g</td></tr>
        <tr><td>Fat, total</td><td>13.7g</td><td>20%</td><td>91.6g</td></tr>
        <tr class="is-sub"><td>- saturated</td><td>1.9g</td><td>8%</td><td>12.8g</td></tr>
        <tr class="is-sub"><td>- trans</td><td>LESS THAN 0.1g</td><td></td><td>LESS THAN 0.1g</td></tr>
        <tr class="is-sub"><td>- polyunsaturated</td><td>1.2g</td><td></td><td>8.2g</td></tr>
        <tr class="is-sub"><td>- omega 3</td><td>0.1g</td><td></td><td>0.7g</td></tr>
        <tr class="is-sub"><td>- monounsaturated</td><td>10.6g</td><td></td><td>70.5g</td></tr>
        <tr class="is-sub"><td>CHOLESTEROL</td><td>0mg</td><td></td><td>0mg</td></tr>
        <tr><td>Carbohydrate</td><td>0.0g</td><td>0%</td><td>0.0g</td></tr>
        <tr class="is-sub"><td>- sugars</td><td>0.0g</td><td>0%</td><td>0.0g</td></tr>
        <tr><td>Sodium</td><td>0mg</td><td>0%</td><td>0mg</td></tr>
      </table>
      <p class="nutrition__note">Note: All values are considered averages unless otherwise indicated.<br>* Percentage daily intakes are based on an average adult diet of 8700kJ. Your daily intakes may be higher or lower depending on your energy needs.</p>
    </div>
    <div class="supply">
      <p class="supply__head">Produced and bottled by</p>
      <p class="supply__line">XOXOXOXOX XOXOXOXOXOX XOXOXOXOXOOX</p>
      <p class="supply__line">OXOXOXOXOXOXO OXOXOXOXOXOX XO</p>
      <div class="supply__gap"></div>
      <p class="supply__head">Imported in Australia by</p>
      <p class="supply__line">OXOX XOXOXOXOXOX XOXOXOX</p>
      <p class="supply__line">XOXOXOXOXOXOXOXO OXOXOXOXOXOX XOXOX</p>
      <div class="supply__gap"></div>
      <p class="supply__head">Lot Code: <strong>XOXOXOXOXOXO</strong></p>
      <div class="supply__gap"></div>
      <p class="supply__head">Best before:</p>
    </div>
  </section>

</div>
</body>
</html>
```